Lumen Harbor Business Card Design Project

We have recently rebranded and would like to design new business cards that incorporate the corporate logo - double sided cards with corporate logo on one side and contact details on the other

Target Market(s)

Sophisticated and high net worth investors and finance industry professionals

Industry/Entity Type

Funds Management

Contact Information for Business Card

The card should prominently feature the company name and logo. Other details will be standard contact details for each staff member - name, address, phone, email, website

Colors
0054AA
0677BA
7BADD7
CADEEF
E8F1F8

Requirements
Must have
• Double-sided design with one side prominently featuring the corporate logo and the other side with all standard contact details

```html
<!DOCTYPE html>
<html lang="en">
<head>
<meta charset="utf-8">
<title>Lumen Harbor Business Card</title>
<link href="https://fonts.googleapis.com/css2?family=Lato:wght@400;700&display=swap" rel="stylesheet">
<style>
  :root {
    --navy: #204573;
    --ink: #4a4a4a;
    --paper: #ffffff;
    --backdrop: #737373;
  }
  * { margin: 0; padding: 0; box-sizing: border-box; }
  html, body { width: 1200px; height: 1200px; overflow: hidden; }
  body { background: var(--backdrop); font-family: "Lato", sans-serif; position: relative; }

  .card { position: absolute; left: 281px; width: 638px; height: 366px; border-radius: 22px; overflow: hidden; }
  .card--front { top: 195px; background: var(--paper); }
  .card--back { top: 639px; background: var(--navy); }

  .brand-row { position: absolute; left: 68px; width: 490px; top: 130px; display: flex; align-items: flex-end; gap: 16px; }
  .brand-row .rule { flex: 1; height: 2px; background: var(--navy); margin-bottom: 4px; }
  .brand-name { font-weight: 700; font-size: 22px; line-height: 1; color: var(--navy); letter-spacing: 0.5px; white-space: nowrap; }

  .person { position: absolute; right: 332px; top: 198px; text-align: right; }
  .person__name { font-weight: 700; font-size: 29px; line-height: 1; color: var(--navy); letter-spacing: 0.3px; white-space: nowrap; }
  .person__title { font-size: 16px; color: var(--ink); margin-top: 4px; }

  .divider { position: absolute; left: 325px; top: 186px; width: 1px; height: 78px; background: var(--ink); }

  .contacts { position: absolute; left: 345px; top: 181px; list-style: none; }
  .contacts li { display: flex; align-items: center; height: 22px; font-size: 14.5px; color: var(--ink); letter-spacing: 0.6px; white-space: nowrap; }
  .contacts svg { width: 12px; height: 12px; margin-right: 10px; fill: var(--navy); flex: none; }

  .address-row { position: absolute; left: 68px; width: 490px; top: 293px; height: 24px; display: flex; align-items: center; gap: 4px; }
  .address-row .rule { flex: 1; min-width: 30px; height: 2px; background: var(--navy); }
  .address { display: flex; align-items: center; font-size: 14.5px; color: var(--ink); letter-spacing: 0.5px; white-space: nowrap; }
  .address svg { width: 10px; height: 14px; margin-right: 5px; fill: var(--navy); flex: none; }

  .back-name { position: absolute; left: 0; right: 0; top: 190px; text-align: center;
    font-weight: 700; font-size: 52px; line-height: 1; color: var(--paper); letter-spacing: 2px; text-transform: uppercase; }
</style>
</head>
<body>
  <section class="card card--front" aria-label="Card front">
    <div class="brand-row">
      <div class="rule"></div>
      <div class="brand-name">Lumen Harbor</div>
      <div class="rule"></div>
    </div>

    <div class="person">
      <div class="person__name">DANIEL REYES</div>
      <div class="person__title">Founder &amp; CEO</div>
    </div>
    <div class="divider"></div>

    <ul class="contacts">
      <li><svg viewBox="0 0 24 24"><path d="M6.6 10.8a15 15 0 0 0 6.6 6.6l2.2-2.2a1 1 0 0 1 1-.25 11.4 11.4 0 0 0 3.6.6 1 1 0 0 1 1 1V20a1 1 0 0 1-1 1A17 17 0 0 1 3 4a1 1 0 0 1 1-1h3.5a1 1 0 0 1 1 1c0 1.25.2 2.45.6 3.6a1 1 0 0 1-.25 1z"/></svg>(555) 014-2231</li>
      <li><svg viewBox="0 0 24 24"><path d="M7 1h10a2 2 0 0 1 2 2v18a2 2 0 0 1-2 2H7a2 2 0 0 1-2-2V3a2 2 0 0 1 2-2zm0 3v14h10V4zm5 15.5a1 1 0 1 0 0 2 1 1 0 0 0 0-2z"/></svg>(555) 014-2231</li>
      <li><svg viewBox="0 0 24 24"><path d="M2 5h20v14H2zm2 2v.5l8 5 8-5V7zm0 2.8V17h16V9.8l-8 5z"/></svg>info@lumenharbor.com</li>
      <li><svg viewBox="0 0 24 24"><path d="M12 2a10 10 0 1 0 0 20 10 10 0 0 0 0-20zm-1 17.9A8 8 0 0 1 4.2 10L9 14.8V16a2 2 0 0 0 2 2zm6.9-2.5A2 2 0 0 0 16 16h-1v-3a1 1 0 0 0-1-1H8v-2h2a1 1 0 0 0 1-1V7h2a2 2 0 0 0 2-2v-.4a8 8 0 0 1 2.9 12.8z"/></svg>lumenharbor.com</li>
    </ul>

    <div class="address-row">
      <div class="rule"></div>
      <div class="address"><svg viewBox="0 0 20 28"><path d="M10 0a10 10 0 0 0-10 10c0 7.5 10 18 10 18s10-10.5 10-18A10 10 0 0 0 10 0zm0 14a4 4 0 1 1 0-8 4 4 0 0 1 0 8z"/></svg>4410 Birchwood Lane, Milford, CT 06460</div>
      <div class="rule"></div>
    </div>
  </section>

  <section class="card card--back" aria-label="Card back">
    <div class="back-name">Lumen Harbor</div>
  </section>
</body>
</html>
```